"Tarvel Mouthguards " Custom-made Mouthguard Business Website

We need an informational website for our mouthguard Business "Tarvel Mouthguards". The logo is navy blue/lime green so want to have colour scheme that goes nicely with this - have uploaded our mouthguard flyer with some information we need to put into the website but I do have more information to put in there.

Target Market(s)

Sports clubs, sportspeople, parents and kids, schools

Industry/Entity Type

Dental, Custom-made Sports Mouthguards

Coding

Number of Pages Required

5+ page

Font styles to use
Serif
Sans Serif

Colors
0054AA
0677BA
7BADD7
CADEEF
E8F1F8
0094D4
00A9DD
6FCCEA
C7EBF8
E9F6FB
00AB8E
00BBA5
67D7C9
C6EFE9
E9F9F6
59FF00
82FF00
B8FF75
E3FFCB
F4FFEA
FFF300
FFF600
FEFA6F
FFFEC7
FFFEE8
FFC000
F8CF3A
FAE287
FDF2CF
FEFAEE
F0912C
F2A743
F7CA91
FBE8D2
FDF5EE
EE7325
F08F49
F5BC92
FAE3D3
FDF4ED

Requirements
Must have
• I want drop down pages, not one scrolling page. Different pages for each heading . Content uploaded - We need a general home page with lots of pictures and info that I'll provide. A page each dedicated to 1) About Us 2) Why choose a custom mouthguard? 3) Gallery 4) Contact Us. Will need logos from "Morvex"
Nice to have
• Mainly use greens and blues, but happy to pop in some yellow/oranges/red oranges if it looks good

```html
<!DOCTYPE html>
<html lang="en">
<head>
<meta charset="utf-8">
<title>Tarvel Mouthguards – Custom-Made Sports Mouthguards</title>
<link href="https://fonts.googleapis.com/css2?family=Krona+One&family=Poppins:wght@400;500;600;700&display=swap" rel="stylesheet">
<style>
:root{
  --navy:#0f2e6e;
  --navy-deep:#0a2560;
  --green:#2fc93a;
  --green-bright:#33cc33;
  --green-dark:#1f9a3c;
  --light:#f2f2f2;
  --footer:#f4f5f7;
  --text:#222;
  --white:#fff;
}
*{box-sizing:border-box;margin:0;padding:0}
html,body{width:1200px;height:4525px;overflow:hidden}
body{position:relative;font-family:"Poppins",sans-serif;color:var(--text);background:var(--white)}
.abs{position:absolute}
.display{font-family:"Krona One",sans-serif;text-transform:uppercase;letter-spacing:-0.5px}
.btn{position:absolute;display:flex;align-items:center;justify-content:center;background:var(--green);color:var(--white);font-weight:700;font-size:15px;text-transform:uppercase}
.rule{position:absolute;height:3px;background:var(--green)}

/* header */
.site-header{position:absolute;left:0;top:0;width:1200px;height:120px;background:var(--white)}
.brand{position:absolute;display:flex;align-items:center;gap:10px;font-family:"Poppins",sans-serif;font-weight:700;color:var(--navy)}
.brand-dot{border-radius:50%;background:var(--green)}
.call{position:absolute;left:705px;top:28px;font-weight:700;font-size:16px;color:var(--navy)}
.call span{color:var(--green)}
.nav{position:absolute;top:82px;left:0;width:1200px;font-weight:700;font-size:14.5px;color:var(--navy)}
.nav a{position:absolute;text-decoration:none;color:inherit}
.nav a.active{color:var(--green)}

/* hero */
.hero{position:absolute;left:0;top:120px;width:1200px;height:585px;background:linear-gradient(100deg,#2f5d2b 0%,#3b7a33 45%,#2d6a2a 100%)}
.hero-photo{position:absolute;left:520px;top:0;width:680px;height:585px;background:radial-gradient(ellipse at 60% 50%,#4a6ab8 0%,#3a5aa0 35%,rgba(60,110,60,0) 70%)}
.hero h1{position:absolute;left:125px;top:118px;color:var(--white);font-size:40px;line-height:48px}
.hero h2{position:absolute;left:127px;top:218px;color:var(--white);font-weight:600;font-size:36px;line-height:41px}
.hero p{position:absolute;left:127px;top:318px;color:var(--white);font-size:15px;font-weight:500}

/* about */
.about-mark{position:absolute;left:160px;top:826px;width:386px;height:386px;border-radius:50%;background:var(--navy)}
.about h2{position:absolute;left:585px;top:858px;font-size:38px;line-height:40px}
.g{color:var(--green)}.n{color:var(--navy)}
.about p{position:absolute;left:585px;top:972px;width:480px;font-size:14px;line-height:25.7px;color:#222}

/* why */
.why{position:absolute;left:0;top:1483px;width:1200px;height:757px;background:linear-gradient(90deg,var(--navy) 0%,#0f4a6a 40%,#1c8f4a 75%,var(--green) 100%);color:var(--white)}
.why h2{position:absolute;left:0;width:1200px;top:72px;text-align:center;font-size:36px;line-height:38px}
.why .center{position:absolute;left:498px;top:333px;width:205px;height:205px;border-radius:50%;background:var(--white)}
.feat-icon{position:absolute;width:72px;height:72px;border-radius:50%;background:var(--green);display:flex;align-items:center;justify-content:center}
.feat{position:absolute;font-size:16.5px;font-weight:500;line-height:20px}
.why .note{position:absolute;left:0;width:1200px;top:645px;text-align:center;font-weight:700;font-size:17.5px;line-height:25px}
.why .note span{color:var(--green)}

/* mouthguards */
.products{position:absolute;left:0;top:2240px;width:1200px;height:568px;background:var(--light)}
.sec-title{position:absolute;left:0;width:1200px;text-align:center;font-size:36px}
.product-img{position:absolute;top:205px;width:230px;height:145px;border-radius:50%}
.product-name{position:absolute;top:375px;width:230px;text-align:center;font-size:18px;color:#333}

/* gallery */
.gallery-img{position:absolute;top:3032px;height:280px}

/* contact */
.contact{position:absolute;left:0;top:3517px;width:1200px;height:608px;background:linear-gradient(120deg,var(--navy) 0%,#0f4a6a 40%,#1c8f4a 70%,var(--green) 100%);color:var(--white)}
.contact h2{position:absolute;left:137px;top:98px;font-size:34px}
.contact .lead{position:absolute;left:137px;top:157px;width:340px;font-size:14px;line-height:18px}
.c-item{position:absolute;left:138px;display:flex;gap:14px;font-size:14px;line-height:17px;width:350px}
.c-item svg{flex:none}
.form{position:absolute;left:672px;top:93px;width:401px;height:350px;background:var(--green-bright);border-radius:8px}
.field{position:absolute;left:33px;width:335px;height:40px;background:var(--white);border-radius:3px;font-size:13px;color:#333;padding:10px 14px}
.submit{position:absolute;left:33px;top:283px;width:335px;height:44px;background:var(--navy-deep);border-radius:3px;color:var(--white);font-weight:700;font-size:15px;display:flex;align-items:center;justify-content:center}

/* footer */
.footer{position:absolute;left:0;top:4125px;width:1200px;height:400px;background:var(--footer)}
.vline{position:absolute;top:45px;width:1px;height:280px;background:#cfd3da}
.f-head{position:absolute;font-family:"Krona One",sans-serif;font-size:21px;color:var(--navy)}
.f-links{position:absolute;left:515px;top:106px;list-style:none;font-size:15px;line-height:28px;color:#333}
.f-item{position:absolute;left:757px;display:flex;gap:14px;font-size:15px;line-height:18px;color:#222;width:360px}
.copy{position:absolute;left:127px;top:352px;font-size:14.5px;color:#222}
.social{position:absolute;top:342px;width:34px;height:34px;border-radius:50%;background:#111}
</style>
</head>
<body>

<header class="site-header">
  <div class="brand" style="left:110px;top:36px;font-size:27px">
    <span class="brand-dot" style="width:26px;height:26px"></span>Tarvel Mouthguards
  </div>
  <div class="call">
    <svg width="14" height="14" viewBox="0 0 24 24" style="vertical-align:-1px"><path fill="#2fc93a" d="M6.6 10.8a15 15 0 0 0 6.6 6.6l2.2-2.2a1 1 0 0 1 1-.25 11.4 11.4 0 0 0 3.6.57 1 1 0 0 1 1 1V20a1 1 0 0 1-1 1A17 17 0 0 1 3 4a1 1 0 0 1 1-1h3.5a1 1 0 0 1 1 1c0 1.25.2 2.45.57 3.57a1 1 0 0 1-.25 1z"/></svg>
    <span>CALL:</span> 08 6000 1234
  </div>
  <div class="btn" style="left:913px;top:20px;width:190px;height:40px;font-size:14px">Book Online Now</div>
  <nav class="nav">
    <a class="active" style="left:373px">HOME</a>
    <a style="left:458px">ABOUT US</a>
    <a style="left:575px">OUR MOUTHGUARDS</a>
    <a style="left:784px">PHOTO GALLERY</a>
    <a style="left:953px">FAQ</a>
    <a style="left:1024px">CONTACT</a>
  </nav>
</header>

<section class="hero">
  <div class="hero-photo" role="img" aria-label="Two kids in football jerseys holding a football and smiling with coloured mouthguards"></div>
  <h1 class="display">Tarvel<br>Mouthguards</h1>
  <h2>Custom-Made Sports<br>Mouthguards in Perth</h2>
  <p>Protect your smile with a comfortable, professional fit.</p>
  <div class="btn" style="left:127px;top:355px;width:158px;height:50px">Book Now</div>
</section>

<section class="about">
  <div class="about-mark" role="img" aria-label="Circular graphic with a smiling mouth wearing a green mouthguard"></div>
  <h2 class="display"><span class="g">About Tarvel</span><br><span class="n">Mouthguards</span></h2>
  <div class="rule" style="left:585px;top:945px;width:150px"></div>
  <p>My name is Elsie, and I am a dental prosthetist with over 20 years of experience in the field dental field. I hold a Diploma of Dental Technology and an Advanced Diploma of Dental Prosthetics, which I obtained at Coastal Institute of Technology in 2011. At Tarvel Mouthguards (inside my Westshore Denture Care clinic), my work involves designing and making custom-fitted sports mouthguards for athletes of all ages.</p>
  <div class="btn" style="left:585px;top:1188px;width:151px;height:50px">Read More</div>
</section>

<section class="why">
  <h2 class="display"><span class="g">Why Choose a</span><br>Custom Mouthguard?</h2>
  <div class="rule" style="left:508px;top:160px;width:184px"></div>
  <div class="center"></div>

  <div class="feat" style="left:470px;top:182px;width:260px;text-align:center">Wide range of colours<br>and designs</div>
  <div class="feat-icon" style="left:564px;top:232px"><svg width="40" height="40" viewBox="0 0 40 40" fill="none" stroke="#fff" stroke-width="2"><path d="M6 16c4 10 24 10 28 0M8 16h24M12 20v4M20 21v5M28 20v4"/></svg></div>

  <div class="feat" style="left:150px;top:332px;width:260px;text-align:right">Custom fit for comfort,<br>protection, and durability</div>
  <div class="feat-icon" style="left:414px;top:320px"><svg width="40" height="40" viewBox="0 0 40 40" fill="none" stroke="#fff" stroke-width="2"><path d="M10 32L30 8M16 26c8-2 14-10 14-18C22 10 14 16 14 24"/></svg></div>

  <div class="feat-icon" style="left:719px;top:320px"><svg width="40" height="40" viewBox="0 0 40 40" fill="none" stroke="#fff" stroke-width="2"><circle cx="14" cy="15" r="6"/><circle cx="27" cy="15" r="6"/><path d="M4 34c0-7 4-11 10-11s10 4 10 11M18 34c0-7 4-11 9-11s9 4 9 11"/></svg></div>
  <div class="feat" style="left:800px;top:332px;width:260px">Available for kids,<br>teens, and adults</div>

  <div class="feat" style="left:140px;top:452px;width:255px;text-align:right">Professionally made by a<br>qualified dental prosthetist</div>
  <div class="feat-icon" style="left:400px;top:437px"><svg width="40" height="40" viewBox="0 0 40 40" fill="none" stroke="#fff" stroke-width="2"><circle cx="16" cy="12" r="6"/><path d="M4 34c0-8 5-12 12-12s12 4 12 12"/><path d="M26 24c2-2 6-2 8 0s1 6-1 10h-2l-1-4-1 4h-2c-2-4-3-8-1-10z"/></svg></div>

  <div class="feat-icon" style="left:719px;top:437px"><svg width="40" height="40" viewBox="0 0 40 40" fill="none" stroke="#fff" stroke-width="2"><rect x="8" y="10" width="24" height="24"/><path d="M17 34v-7h6v7M20 14v6M17 17h6M12 24h3M25 24h3"/></svg></div>
  <div class="feat" style="left:802px;top:452px;width:300px;font-weight:700">Clinic and mobile school/club<br>visits available</div>

  <p class="note">Talk to us about our “<span>gap free</span>” mouthguards for<br>eligible private health insurance members.</p>
</section>

<section class="products">
  <h2 class="sec-title display" style="top:82px"><span class="g">Our</span> <span class="n">Mouthguards</span></h2>
  <div class="rule" style="left:510px;top:148px;width:180px"></div>
  <div class="product-img" style="left:78px;background:radial-gradient(circle,#d9a3c8,#8ab6e0)" role="img" aria-label="Pink and blue marbled mouthguard"></div>
  <div class="product-img" style="left:355px;background:radial-gradient(circle,#e06060,#555)" role="img" aria-label="Red, white and black patterned mouthguard"></div>
  <div class="product-img" style="left:632px;background:radial-gradient(circle,#f2d12a,#2d62c7)" role="img" aria-label="Blue and yellow mouthguard"></div>
  <div class="product-img" style="left:900px;background:radial-gradient(circle,#8a8a8a,#c7a9c7)" role="img" aria-label="Glitter mouthguards in mixed colours"></div>
  <div class="product-name" style="left:80px">Mouthguard Name</div>
  <div class="product-name" style="left:359px">Mouthguard Name</div>
  <div class="product-name" style="left:636px">Mouthguard Name</div>
  <div class="product-name" style="left:915px">Mouthguard Name</div>
  <div class="btn" style="left:525px;top:455px;width:151px;height:50px">View All</div>
</section>

<section class="gallery">
  <h2 class="sec-title display" style="top:2925px"><span class="g">Photo</span> <span class="n">Gallery</span></h2>
  <div class="rule" style="left:520px;top:2990px;width:160px"></div>
  <div class="gallery-img" style="left:127px;width:270px;background:linear-gradient(160deg,#e8e2dc,#9b2a45 70%)" role="img" aria-label="Maroon school mouthguards in a white case"></div>
  <div class="gallery-img" style="left:418px;width:363px;background:linear-gradient(90deg,#c8151b 0%,#7a1d16 45%,#e8e6e3 60%,#f0b7c0 100%)" role="img" aria-label="Mouthguards in red and white cases"></div>
  <div class="gallery-img" style="left:802px;width:271px;background:linear-gradient(160deg,#d8d3df,#7c4bb5 60%)" role="img" aria-label="Purple glitter mouthguard held in a hand"></div>
  <div class="btn" style="left:525px;top:3355px;width:151px;height:50px">View More</div>
</section>

<section class="contact">
  <h2 class="display">Contact Us</h2>
  <p class="lead">Please contact us to make a booking for your new custom mouthguard.</p>
  <div class="c-item" style="top:213px"><svg width="18" height="20" viewBox="0 0 24 24" fill="none" stroke="#2fc93a" stroke-width="2"><path d="M12 22s7-7 7-12a7 7 0 0 0-14 0c0 5 7 12 7 12z"/><circle cx="12" cy="10" r="2.5"/></svg><span>Clinic: Tarvel Mouthguards at Westshore Denture Care</span></div>
  <div class="c-item" style="top:268px"><svg width="18" height="18" viewBox="0 0 24 24" fill="none" stroke="#2fc93a" stroke-width="2"><path d="M6.6 10.8a15 15 0 0 0 6.6 6.6l2.2-2.2 4.6 1.3V20a1 1 0 0 1-1 1A17 17 0 0 1 3 4a1 1 0 0 1 1-1h3.5l1.3 4.6z"/></svg><span>Phone: (08) 6000 1234</span></div>
  <div class="c-item" style="top:304px"><svg width="18" height="16" viewBox="0 0 24 20" fill="none" stroke="#2fc93a" stroke-width="2"><rect x="2" y="2" width="20" height="16"/><path d="M2 2l10 9 10-9"/></svg><span>Email: info@tarvelmouthguards.com.au</span></div>
  <div class="c-item" style="top:353px"><svg width="18" height="20" viewBox="0 0 24 24" fill="none" stroke="#2fc93a" stroke-width="2"><path d="M12 22s7-7 7-12a7 7 0 0 0-14 0c0 5 7 12 7 12z"/><circle cx="12" cy="10" r="2.5"/></svg><span>Address: Unit 5, 12 Harbour Crescent, Kelmont, Western Australia, 6091</span></div>
  <div class="btn" style="left:138px;top:408px;width:175px;height:40px;font-size:13.5px">Book Online Now</div>

  <form class="form">
    <div class="field" style="top:27px">Name:</div>
    <div class="field" style="top:82px">Email:</div>
    <div class="field" style="top:137px">Phone:</div>
    <div class="field" style="top:192px;height:76px">Message:</div>
    <div class="submit">SUBMIT NOW</div>
  </form>
</section>

<svg class="abs" style="left:0;top:4040px" width="1200" height="90" viewBox="0 0 1200 90">
  <polygon points="0,0 1200,45 1200,90 0,90" fill="#1e4f8a"/>
  <polygon points="0,25 420,55 0,90" fill="#2fc93a"/>
</svg>

<footer class="footer">
  <div class="brand" style="left:135px;top:70px;font-size:30px;width:290px;flex-wrap:wrap">
    <span class="brand-dot" style="width:28px;height:28px"></span>Tarvel<br>Mouthguards
  </div>
  <div class="brand" style="left:160px;top:193px;font-size:28px;font-weight:500;color:#222">
    <span class="brand-dot" style="width:22px;height:22px;background:#f2d12a"></span>Morvex
  </div>
  <div class="vline" style="left:453px"></div>
  <div class="vline" style="left:702px"></div>

  <div class="f-head" style="left:515px;top:62px">Links</div>
  <ul class="f-links">
    <li>Home</li><li>About Us</li><li>Our Mouthguards</li><li>Photo Gallery</li><li>FAQ</li><li>Contact</li>
  </ul>

  <div class="f-head" style="left:757px;top:50px">Contact</div>
  <div class="f-item" style="top:101px"><svg width="16" height="18" viewBox="0 0 24 24" fill="#2fc93a"><path d="M12 22s7-7 7-12a7 7 0 0 0-14 0c0 5 7 12 7 12z"/></svg><span>Clinic: Tarvel Mouthguards at<br>Westshore Denture Care</span></div>
  <div class="f-item" style="top:157px"><svg width="16" height="16" viewBox="0 0 24 24" fill="#2fc93a"><path d="M6.6 10.8a15 15 0 0 0 6.6 6.6l2.2-2.2 4.6 1.3V20a1 1 0 0 1-1 1A17 17 0 0 1 3 4a1 1 0 0 1 1-1h3.5l1.3 4.6z"/></svg><span>Phone: (08) 6000 1234</span></div>
  <div class="f-item" style="top:197px"><svg width="16" height="14" viewBox="0 0 24 20" fill="#2fc93a"><rect x="2" y="2" width="20" height="16"/></svg><span>Email: info@tarvelmouthguards.com.au</span></div>
  <div class="f-item" style="top:237px"><svg width="16" height="18" viewBox="0 0 24 24" fill="#2fc93a"><path d="M12 22s7-7 7-12a7 7 0 0 0-14 0c0 5 7 12 7 12z"/></svg><span>Address: Unit 5, 12 Harbour Crescent,<br>Kelmont, Western Australia, 6091</span></div>

  <p class="copy">Copyright © 2025 Tarvel Mouthguards. All Rights Reserved.</p>
  <span class="social" style="left:700px"></span>
  <span class="social" style="left:740px"></span>
  <span class="social" style="left:780px"></span>
  <span class="social" style="left:820px"></span>
  <div class="abs" style="left:895px;top:348px;font-size:16px;font-weight:600;color:#3aa9d8">Westshore Denture Care</div>
</footer>

</body>
</html>
```